Crestline Gas and Plumbing Business Card Design

I am after a business card design for my plumbing business called 'Crestline Gas & Plumbing'. I do all types of plumbing and gas work and specialise in general maintenance plumbing. Would like to see designs using current logo

Industry/Entity Type

Plumbing

Contact Information for Business Card

Name - Dale Whitcombe
Phone number - 0455163027
Email - admin@crestlinegasandplumbing.example.com.au
ABN - 68204915336

```html
<!DOCTYPE html>
<html lang="en">
<head>
<meta charset="utf-8">
<title>Crestline Gas &amp; Plumbing – Business Card</title>
<link href="https://fonts.googleapis.com/css2?family=Open+Sans:wght@400;600;700&display=swap" rel="stylesheet">
<style>
  :root {
    --page-bg: #ece7e1;
    --card-white: #ffffff;
    --card-shadow: rgba(40, 25, 10, 0.25);
    --accent-yellow: #f7c614;
    --accent-orange: #f08a2a;
    --accent-red: #e2452a;
    --icon-blue: #1f3f9c;
    --white: #ffffff;
  }
  * { margin: 0; padding: 0; box-sizing: border-box; }
  html, body {
    width: 1200px; height: 1200px; overflow: hidden;
    background: var(--page-bg);
    font-family: "Open Sans", Arial, sans-serif;
  }
  .canvas { position: relative; width: 1200px; height: 1200px; }

  .card {
    position: absolute;
    box-shadow: 0 6px 14px var(--card-shadow);
  }

  /* Contact side */
  .card--contact {
    left: 376px; top: 150px; width: 624px; height: 348px;
    background: linear-gradient(160deg, #ffffff 40%, #eeeeee 100%);
  }
  .card__brand {
    position: absolute; left: 30px; top: 140px; width: 210px;
    display: flex; align-items: center; gap: 10px;
    font-weight: 700; font-size: 30px; color: var(--accent-orange);
  }
  .card__brand-dot {
    width: 16px; height: 16px; border-radius: 50%;
    background: var(--accent-orange); flex: none;
  }
  .card__divider {
    position: absolute; left: 253px; top: 25px; width: 9px; height: 296px;
    background: linear-gradient(to bottom, var(--accent-yellow), var(--accent-orange) 60%, var(--accent-red));
  }
  .gradient-text {
    background: linear-gradient(to bottom, var(--accent-yellow) 20%, var(--accent-orange) 80%, var(--accent-red));
    -webkit-background-clip: text; background-clip: text;
    color: transparent;
  }
  .card__name {
    position: absolute; left: 288px; top: 34px;
    font-size: 50px; line-height: 56px; font-weight: 400;
  }
  .card__name span { display: block; }
  .card__name .surname { padding-left: 50px; }
  .contact-row {
    position: absolute; left: 276px;
    display: flex; align-items: center;
  }
  .contact-row--phone { top: 146px; }
  .contact-row--email { top: 210px; }
  .contact-row--abn { top: 270px; }
  .contact-row__icon { width: 44px; height: 36px; flex: none; }
  .contact-row__label {
    width: 60px; font-size: 22px; font-weight: 600; color: var(--icon-blue);
  }
  .contact-row__value { font-size: 21px; margin-left: 22px; }
  .contact-row--email .contact-row__value { font-size: 11.5px; font-weight: 600; margin-left: 16px; }
  .contact-row--abn .contact-row__value { margin-left: 6px; }

  /* Brand side */
  .card--brand {
    left: 115px; top: 618px; width: 623px; height: 352px;
    background: linear-gradient(to bottom, #fdd11a 0%, #f7a521 45%, #ed7a31 80%, #e4562a 100%);
  }
  .card--brand .brand-name {
    position: absolute; left: 58px; top: 120px;
    display: flex; align-items: center; gap: 22px;
    color: var(--white); font-weight: 700;
  }
  .brand-name__square {
    width: 34px; height: 34px; background: var(--white); flex: none;
  }
  .brand-name__text { font-size: 52px; line-height: 58px; }
  .brand-name__text span { display: block; font-size: 30px; line-height: 40px; }
</style>
</head>
<body>
<main class="canvas">

  <section class="card card--contact" aria-label="Business card contact side">
    <div class="card__brand"><span class="card__brand-dot"></span>Crestline</div>
    <div class="card__divider"></div>

    <h1 class="card__name gradient-text">
      <span>Dale</span>
      <span class="surname">Whitcombe</span>
    </h1>

    <div class="contact-row contact-row--phone">
      <svg class="contact-row__icon" viewBox="0 0 44 36" aria-hidden="true">
        <path d="M8 4 C4 6 4 12 8 18 C13 26 20 32 28 33 C31 33 33 31 33 29 L28 24 C26 23 25 24 24 26 C19 24 14 18 13 13 C15 12 16 11 15 9 Z" fill="var(--icon-blue)"/>
      </svg>
      <span class="contact-row__value gradient-text">0455163027</span>
    </div>

    <div class="contact-row contact-row--email">
      <svg class="contact-row__icon" viewBox="0 0 44 36" aria-hidden="true">
        <rect x="2" y="3" width="40" height="30" fill="none" stroke="var(--icon-blue)" stroke-width="3"/>
        <path d="M2 3 L22 20 L42 3 M2 33 L17 16 M42 33 L27 16" fill="none" stroke="var(--icon-blue)" stroke-width="2.5"/>
      </svg>
      <span class="contact-row__value gradient-text">admin@crestlinegasandplumbing.example.com.au</span>
    </div>

    <div class="contact-row contact-row--abn">
      <span class="contact-row__label">ABN</span>
      <span class="contact-row__value gradient-text">68204915336</span>
    </div>
  </section>

  <section class="card card--brand" aria-label="Business card brand side">
    <div class="brand-name">
      <span class="brand-name__square"></span>
      <div class="brand-name__text">Crestline<span>Gas &amp; Plumbing</span></div>
    </div>
  </section>

</main>
</body>
</html>
```